Photoshop Design for Z-Volt Energy Drink

Providing energy soft drink. We are targeting clubs and bars. Hence any design has to be focused on these two areas.

```html
<!DOCTYPE html>
<html lang="en">
<head>
<meta charset="utf-8">
<title>Z-Volt Energy Drink – Can Label</title>
<link rel="stylesheet" href="https://fonts.googleapis.com/css2?family=Archivo+Black&family=Oswald:wght@500&display=swap">
<style>
  :root {
    --page-bg: #ffffff;
    --label-deep: #0a1422;
    --label-navy: #1a2c44;
    --label-steel: #3d5878;
    --label-glow: #93a9c4;
    --brand-white: #f1f1ec;
    --tagline-red: #e0413a;
  }
  * { margin: 0; padding: 0; box-sizing: border-box; }
  html, body {
    width: 1200px;
    height: 972px;
    overflow: hidden;
    background: var(--page-bg);
  }
  .canvas {
    position: relative;
    width: 1200px;
    height: 972px;
  }
  .can-label {
    position: absolute;
    left: 330px;
    top: 66px;
    width: 540px;
    height: 840px;
    overflow: hidden;
    background: var(--label-deep);
  }
  .label-artwork {
    position: absolute;
    inset: 0;
    display: block;
  }
  .brand-name {
    position: absolute;
    top: 40px;
    bottom: 56px;
    left: 160px;
    width: 190px;
    writing-mode: vertical-rl;
    transform: rotate(180deg);
    font-family: "Archivo Black", sans-serif;
    font-weight: 400;
    font-size: 200px;
    line-height: 190px;
    letter-spacing: -4px;
    color: var(--brand-white);
    white-space: nowrap;
  }
  .tagline {
    position: absolute;
    top: 40px;
    bottom: 56px;
    left: 372px;
    width: 62px;
    writing-mode: vertical-rl;
    transform: rotate(180deg);
    font-family: "Oswald", sans-serif;
    font-weight: 500;
    font-size: 52px;
    line-height: 62px;
    letter-spacing: 9px;
    color: var(--tagline-red);
    white-space: nowrap;
  }
</style>
</head>
<body>
  <main class="canvas">
    <section class="can-label">
      <svg class="label-artwork" viewBox="0 0 540 840" preserveAspectRatio="none" role="img" aria-label="Dark blue energy swirl with white lightning bolts, glowing bubbles and a paint splatter">
        <defs>
          <radialGradient id="swirl-glow" cx="0.5" cy="0.38" r="0.8">
            <stop offset="0" stop-color="var(--label-glow)"/>
            <stop offset="0.3" stop-color="var(--label-steel)"/>
            <stop offset="0.65" stop-color="var(--label-navy)"/>
            <stop offset="1" stop-color="var(--label-deep)"/>
          </radialGradient>
          <radialGradient id="corner-shade" cx="0.05" cy="0.75" r="0.45">
            <stop offset="0" stop-color="var(--label-deep)" stop-opacity="0.9"/>
            <stop offset="1" stop-color="var(--label-deep)" stop-opacity="0"/>
          </radialGradient>
          <radialGradient id="side-glow" cx="0.85" cy="0.55" r="0.35">
            <stop offset="0" stop-color="var(--label-steel)" stop-opacity="0.7"/>
            <stop offset="1" stop-color="var(--label-steel)" stop-opacity="0"/>
          </radialGradient>
        </defs>
        <rect width="540" height="840" fill="url(#swirl-glow)"/>
        <rect width="540" height="840" fill="url(#side-glow)"/>
        <rect width="540" height="840" fill="url(#corner-shade)"/>
      </svg>
      <h1 class="brand-name">Z-Volt</h1>
      <p class="tagline">I NEED SOME ENERGY</p>
    </section>
  </main>
</body>
</html>
```